Tallwater Marketing Business Card

Business card using new logo for marketing consulting company based in Silicon Valley. Limited information on card now (name, phone number, email, website), but room to add mailing address later.

```html
<!DOCTYPE html>
<html lang="en">
<head>
<meta charset="utf-8">
<title>Tallwater Marketing – Business Card</title>
<link rel="stylesheet" href="https://fonts.googleapis.com/css2?family=Open+Sans:wght@400;600&display=swap">
<style>
  :root {
    --canvas: #e9e7e4;
    --navy-deep: #143d6b;
    --navy-light: #2f5f93;
    --cyan: #2bb3e6;
    --paper: #ffffff;
    --paper-shade: #eeeeef;
    --ink: #2a2d33;
    --rule: #5a7394;
    --white: #ffffff;
  }
  * { margin: 0; padding: 0; box-sizing: border-box; }
  html, body {
    width: 1200px;
    height: 800px;
    overflow: hidden;
    background: var(--canvas);
    font-family: "Open Sans", Arial, sans-serif;
  }
  .stage {
    position: relative;
    width: 1200px;
    height: 800px;
  }
  .card {
    position: absolute;
    overflow: hidden;
    box-shadow: 0 6px 18px rgba(0,0,0,0.18);
  }

  /* Front: vertical navy card */
  .card-front {
    left: 130px;
    top: 130px;
    width: 330px;
    height: 540px;
    background: linear-gradient(160deg, var(--navy-light) 0%, var(--navy-deep) 70%);
    color: var(--white);
  }
  .front-brand {
    position: absolute;
    top: 70px;
    left: 0;
    right: 0;
    display: flex;
    flex-direction: column;
    align-items: center;
    gap: 16px;
  }
  .brand-dot {
    width: 64px;
    height: 64px;
    border-radius: 50%;
    background: var(--white);
  }
  .front-brand .brand-name {
    font-size: 20px;
    font-weight: 400;
    letter-spacing: 3px;
    text-transform: uppercase;
    color: var(--white);
  }
  .front-person {
    position: absolute;
    left: 238px;
    top: 250px;
    transform-origin: 0 0;
    transform: rotate(90deg);
    white-space: nowrap;
    line-height: 1.2;
  }
  .person-name {
    font-size: 40px;
    font-weight: 600;
    letter-spacing: 1px;
    text-transform: uppercase;
  }
  .person-title {
    margin-top: 4px;
    font-size: 20px;
    font-weight: 400;
    letter-spacing: 2px;
    text-transform: uppercase;
  }

  /* Back: horizontal white card */
  .card-back {
    left: 520px;
    top: 230px;
    width: 560px;
    height: 340px;
    background: radial-gradient(circle at 80% 75%, var(--paper-shade) 0%, var(--paper) 55%);
    color: var(--ink);
  }
  .back-brand {
    position: absolute;
    left: 40px;
    top: 0;
    bottom: 0;
    width: 230px;
    display: flex;
    flex-direction: column;
    align-items: center;
    justify-content: center;
    gap: 14px;
  }
  .back-brand .brand-dot {
    width: 48px;
    height: 48px;
    background: var(--cyan);
  }
  .back-brand .brand-name {
    font-size: 26px;
    font-weight: 400;
    line-height: 1.15;
    text-align: center;
    text-transform: uppercase;
    color: var(--cyan);
  }
  .divider {
    position: absolute;
    left: 290px;
    top: 70px;
    width: 1px;
    height: 200px;
    background: var(--rule);
  }
  .contact {
    position: absolute;
    left: 315px;
    top: 105px;
    font-size: 14px;
    line-height: 1.6;
    list-style: none;
  }
  .contact-item {
    display: flex;
    align-items: center;
    gap: 8px;
  }
  .contact-icon {
    width: 14px;
    height: 14px;
    flex: none;
  }
  .address {
    position: absolute;
    left: 315px;
    top: 200px;
    font-size: 14px;
    line-height: 1.6;
    font-style: normal;
    text-transform: uppercase;
  }
</style>
</head>
<body>
<main class="stage">

  <section class="card card-front" aria-label="Business card front">
    <div class="front-brand">
      <span class="brand-dot"></span>
      <span class="brand-name">Tallwater</span>
    </div>
    <div class="front-person">
      <h1 class="person-name">Marcus Yee</h1>
      <p class="person-title">Director</p>
    </div>
  </section>

  <section class="card card-back" aria-label="Business card back">
    <div class="back-brand">
      <span class="brand-dot"></span>
      <span class="brand-name">Tallwater<br>Marketing</span>
    </div>
    <span class="divider"></span>
    <ul class="contact">
      <li class="contact-item">
        <svg class="contact-icon" viewBox="0 0 14 14" aria-hidden="true">
          <circle cx="7" cy="7" r="7" fill="#143d6b"/>
          <path d="M4.5 3.5l1.5 0.2 0.5 1.8-0.9 0.7a5 5 0 0 0 2.2 2.2l0.7-0.9 1.8 0.5 0.2 1.5c-3.5 0.5-6.7-2.5-6-6z" fill="#fff"/>
        </svg>
        +1 415 555 0187
      </li>
      <li class="contact-item">
        <svg class="contact-icon" viewBox="0 0 14 14" aria-hidden="true">
          <circle cx="7" cy="7" r="7" fill="#143d6b"/>
          <rect x="3.5" y="4.5" width="7" height="5" fill="none" stroke="#fff" stroke-width="1"/>
          <path d="M3.5 4.5l3.5 3 3.5-3" fill="none" stroke="#fff" stroke-width="1"/>
        </svg>
        marcus@tallwater-mkt.com
      </li>
      <li class="contact-item">
        <svg class="contact-icon" viewBox="0 0 14 14" aria-hidden="true">
          <circle cx="7" cy="7" r="7" fill="#143d6b"/>
          <circle cx="7" cy="7" r="4" fill="none" stroke="#fff" stroke-width="0.9"/>
          <ellipse cx="7" cy="7" rx="1.8" ry="4" fill="none" stroke="#fff" stroke-width="0.9"/>
          <path d="M3 7h8" stroke="#fff" stroke-width="0.9"/>
        </svg>
        www.tallwater-mkt.com
      </li>
    </ul>
    <address class="address">
      42 Harlow Ave<br>
      Palo Alto CA 94301
    </address>
  </section>

</main>
</body>
</html>
```